Luxury Brand Real Estate For Sale sign

**Update** I've added some examples from the internet of other signs that have a look similar to what I would like to see. I do not want my personal name in the sign. And the word FOR SALE Does not need to be so large - it can be more subtle.
I want to create a Real Estate for sale sign for my company that will be used for luxury/higher end real estate listings. I’m sharing my business card as well as a logo with new teal color to show what we're moving towards: we’re using Teal, white, black and gold.
Hoping the sign is simple, sophisticated and eye catching.
The sign should be 24" wide by 30" tall including the company name: Harbor Crest Realty Group and our logo, office phone number 727-555-0148 and website www.hcrgexample.com the words "For Sale"
Optional to add this e-mail address info@hcrgexample.com to the sign
Target Market(s)
Luxury home buyers
Industry/Entity Type
Real Estate
Look and feel

```html
<!DOCTYPE html>
<html lang="en">
<head>
<meta charset="utf-8">
<title>Harbor Crest Realty Group – For Sale Sign</title>
<link rel="stylesheet" href="https://fonts.googleapis.com/css2?family=Montserrat:wght@500;600;700;800&family=Raleway:wght@300;400&display=swap">
<style>
  :root {
    --gold: #dba61f;
    --black: #000000;
    --white: #ffffff;
    --page: #ffffff;
  }
  * { margin: 0; padding: 0; box-sizing: border-box; }
  html, body {
    width: 1200px;
    height: 1000px;
    overflow: hidden;
    background: var(--page);
  }
  .sign {
    position: absolute;
    left: 306px;
    top: 133px;
    width: 588px;
    height: 734px;
    background: var(--black);
    font-family: "Montserrat", sans-serif;
  }
  .sign-header {
    position: absolute;
    left: 0; top: 0;
    width: 588px; height: 145px;
    background: var(--black);
  }
  .brand-mark {
    position: absolute;
    left: 52px; top: 54px;
    display: flex;
    align-items: center;
    gap: 10px;
  }
  .brand-square {
    width: 14px; height: 14px;
    background: var(--gold);
  }
  .brand-initials {
    font-family: "Raleway", sans-serif;
    font-weight: 300;
    font-size: 38px;
    line-height: 1;
    color: var(--white);
    letter-spacing: 1px;
  }
  .header-divider {
    position: absolute;
    left: 197px; top: 0;
    width: 2px; height: 145px;
    background: var(--white);
  }
  .company-name {
    position: absolute;
    left: 224px; top: 50px;
    font-family: "Raleway", sans-serif;
    font-weight: 300;
    font-size: 30px;
    line-height: 1;
    color: var(--gold);
    letter-spacing: 0.5px;
    white-space: nowrap;
  }
  .company-sub {
    position: absolute;
    left: 224px; top: 86px;
    font-family: "Raleway", sans-serif;
    font-weight: 400;
    font-size: 15px;
    line-height: 1;
    color: var(--white);
    letter-spacing: 7.5px;
    white-space: nowrap;
  }
  .headline-band {
    position: absolute;
    left: 0; top: 145px;
    width: 588px; height: 309px;
    background: var(--gold);
  }
  .headline {
    position: absolute;
    left: 54px; top: 52px;
    font-weight: 800;
    font-size: 112px;
    line-height: 105px;
    color: var(--black);
    letter-spacing: -1px;
  }
  .contact-band {
    position: absolute;
    left: 0; top: 454px;
    width: 588px; height: 210px;
    background: var(--black);
    text-align: center;
    color: var(--white);
  }
  .phone {
    position: absolute;
    left: 0; right: 0; top: 54px;
    font-weight: 700;
    font-size: 78px;
    line-height: 1;
    letter-spacing: -2px;
  }
  .email {
    position: absolute;
    left: 0; right: 0; top: 132px;
    font-weight: 600;
    font-size: 30px;
    line-height: 1;
  }
  .web-band {
    position: absolute;
    left: 0; top: 664px;
    width: 588px; height: 70px;
    background: var(--gold);
    display: flex;
    align-items: center;
    justify-content: center;
  }
  .website {
    font-weight: 600;
    font-size: 24px;
    color: var(--black);
    letter-spacing: 6px;
    margin-right: -6px;
  }
</style>
</head>
<body>
  <div class="sign">
    <header class="sign-header">
      <div class="brand-mark">
        <span class="brand-square"></span>
        <span class="brand-initials">HCRG</span>
      </div>
      <div class="header-divider"></div>
      <div class="company-name">HARBOR CREST</div>
      <div class="company-sub">REALTY GROUP</div>
    </header>
    <section class="headline-band">
      <h1 class="headline">FOR<br>SALE</h1>
    </section>
    <section class="contact-band">
      <div class="phone">727-555-0148</div>
      <div class="email">info@hcrgexample.com</div>
    </section>
    <footer class="web-band">
      <span class="website">www.hcrgexample.com</span>
    </footer>
  </div>
</body>
</html>
```